Lumen Keyvault Password Manager WebApp Design

Lumen Keyvault is seeking an expert UI designer to provide a fresh and modern visual appeal for our product. Our inspiration comes from two major tools that have successfully managed to balance functionality and design aesthetics - Orbix Folder and Vaultmint. We want our application to exude a similar trustworthiness and modernity, through a clean, intuitive and responsive design.
We have established preliminary mockups and would like the designer to work within these parameters while enhancing the overall user experience. The primary tasks will involve innovative and improved designs of the login screen and the password screen, both being crucial touchpoints for our users. The login screen also serves a crucial role in demonstrating how our system works.
Key Elements:
Logo Integration: We are providing the logo for Lumen Keyvault. The design should align with the logo, both in terms of colors and overall aesthetic, to ensure a cohesive brand identity.
Color Palette: The UI design should adhere to the color palette derived from the logo to maintain brand consistency. The design should effectively utilize these colors to highlight important elements and improve user engagement.
Trustworthy and Modern Design: The UI should be professional and trustworthy. It should mirror the look and feel of Orbix Folder's simplicity and Vaultmint's solid security design, which inspires user confidence.
Adherence to Mockup Boundaries: The existing mockups serve as a guideline for the layout and placement of elements. The design should respect these boundaries while bringing innovation and visual appeal.
Improved Login Screen: The login screen is a key part of the user's journey and should be designed with utmost care. It should be intuitive, easy-to-use, visually engaging, and educative, showcasing how the system operates and encouraging users to sign in with confidence.
Enhanced Password Screen: The password screen, another key user touchpoint, needs improvement. The different types of passwords should be made more visible and intuitive, easing user interaction and enhancing the overall experience.
Prospective designers are encouraged to test our current version available for free at app.lumenkeyvault.com to understand the product better and contribute to meaningful design enhancements.
The goal of this project is to provide a visually compelling and user-friendly interface for Lumen Keyvault that inspires user trust, while adhering to the branding elements, including color scheme and logo design. The ideal designer will have a proven track record of creating compelling UI designs that enhance user experience and engagement.
We preferred the design to be in Figma.
Please provide the 3 design so we can evaluate if we like to choice you:
1. Login Page.
2. Passwords View design
3. Single Passwod Page
We need all the pages to be design that are provided as screenshots.

```html
<!DOCTYPE html>
<html lang="en">
<head>
<meta charset="utf-8">
<title>Lumen Keyvault – Login &amp; Vault</title>
<link rel="stylesheet" href="https://fonts.googleapis.com/css2?family=Inter:wght@400;500;600;700&display=swap">
<style>
  :root {
    --page-bg: #dde6ef;
    --surface: #ffffff;
    --app-bg: #f1f4f8;
    --card-bg: #f3f6fa;
    --brand: #3795f0;
    --brand-soft: #d9eafb;
    --ink: #1f2329;
    --ink-soft: #4a4f57;
    --muted: #8a9099;
    --line: #dfe3e8;
  }
  * { box-sizing: border-box; margin: 0; padding: 0; }
  html, body { width: 1200px; height: 1200px; overflow: hidden; }
  body { background: var(--page-bg); font-family: "Inter", sans-serif; color: var(--ink); position: relative; }
  .abs { position: absolute; }

  /* ---------- Login screen ---------- */
  .login { left: 184px; top: 119px; width: 833px; height: 468px; background: var(--surface); }
  .login-showcase { left: 0; top: 0; width: 512px; height: 468px; border-right: 6px solid #eef4fb; }
  .showcase-art { left: 117px; top: 67px; width: 298px; height: 283px;
    background: radial-gradient(ellipse at 55% 50%, #cfe4fa 0%, #e3effb 55%, #ffffff 80%); border-radius: 46% 54% 48% 52%; }
  .carousel-dots { left: 244px; top: 381px; display: flex; gap: 11px; }
  .carousel-dots span { width: 5px; height: 5px; border-radius: 50%; background: #cfd4da; }
  .carousel-dots span.active { background: var(--brand); }

  .brand { display: flex; align-items: center; gap: 10px; color: var(--brand); font-weight: 500; line-height: 1; white-space: nowrap; }
  .brand-mark { width: 22px; height: 22px; background: var(--brand); border-radius: 4px; flex: none; }
  .login-brand { left: 603px; top: 49px; font-size: 15px; }

  .welcome { left: 512px; width: 321px; top: 123px; text-align: center; font-size: 15px; font-weight: 600; line-height: 18px; }
  .field { left: 573px; width: 203px; height: 25px; border: 1px solid var(--line); border-radius: 5px;
    display: flex; align-items: center; padding: 0 8px; gap: 8px; font-size: 8px; color: var(--muted); }
  .field svg { width: 10px; height: 10px; }
  .field .link { margin-left: auto; color: var(--brand); }
  .field-email { top: 157px; }
  .field-password { top: 197px; }
  .btn-primary { background: var(--brand); color: #fff; border-radius: 5px; display: flex; align-items: center;
    justify-content: center; font-size: 8.5px; font-weight: 600; box-shadow: 0 5px 10px rgba(55,149,240,.25); }
  .btn-login { left: 573px; top: 237px; width: 203px; height: 24px; }
  .or { left: 512px; width: 321px; top: 280px; text-align: center; font-size: 8px; font-weight: 600; }
  .btn-alt { left: 573px; top: 299px; width: 203px; height: 24px; border: 1px solid var(--line); border-radius: 5px;
    display: flex; align-items: center; justify-content: center; font-size: 8.5px; font-weight: 600; color: var(--brand); }
  .signup-prompt { left: 577px; top: 340px; font-size: 8.5px; }
  .btn-signup { left: 686px; top: 332px; width: 90px; height: 25px; }
  .help { left: 512px; width: 321px; top: 416px; display: flex; flex-direction: column; align-items: center; gap: 6px;
    font-size: 8.5px; color: var(--muted); }
  .help-mark { width: 16px; height: 16px; background: #9aa1aa; border-radius: 3px; }

  /* ---------- Vault screen ---------- */
  .vault { left: 184px; top: 658px; width: 833px; height: 468px; background: var(--app-bg); }
  .vault-brand { left: 14px; top: 25px; font-size: 15px; }
  .vault-brand .brand-mark { width: 26px; height: 26px; background: #fff; border: 6px solid var(--brand); }
  .search { left: 174px; top: 20px; width: 448px; height: 36px; background: var(--surface); border-radius: 6px;
    padding: 0 22px; display: flex; align-items: center; font-size: 8.5px; color: var(--muted); }
  .btn-add { left: 642px; top: 20px; width: 88px; height: 36px; gap: 10px; font-size: 12.5px; font-weight: 500; box-shadow: none; }
  .btn-add svg { width: 15px; height: 15px; }
  .bell { left: 756px; top: 29px; width: 14px; height: 14px; }

  .nav-item { left: 14px; width: 140px; height: 29px; display: flex; align-items: center; gap: 20px; padding-left: 12px;
    font-size: 8.5px; color: var(--ink-soft); border-radius: 5px; }
  .nav-item svg { width: 13px; height: 13px; }
  .nav-item.active { background: var(--brand); color: #fff; font-weight: 600; }
  .nav-vault { top: 74px; }
  .nav-shared { top: 112px; }
  .nav-trash { top: 147px; }
  .account { left: 26px; top: 427px; display: flex; align-items: center; gap: 14px; font-size: 8.5px; color: var(--ink-soft); }
  .account svg { width: 13px; height: 13px; }
  .avatar { width: 25px; height: 25px; border-radius: 50%; background: linear-gradient(135deg, #3ab0d8, #7a4a3a); }

  .main-panel { left: 174px; top: 74px; width: 448px; height: 394px; background: var(--surface); border-radius: 6px 6px 0 0; }
  .panel-title { font-size: 12.5px; font-weight: 600; }
  .category-title { left: 22px; top: 8px; }
  .kebab { width: 3px; display: flex; flex-direction: column; gap: 2px; }
  .kebab i { width: 3px; height: 3px; border-radius: 50%; background: currentColor; }
  .category-menu { left: 418px; top: 12px; color: var(--ink); }
  .chips { left: 15px; top: 43px; display: flex; gap: 22px; }
  .chip { height: 22px; border: 1px solid #c9ced5; border-radius: 6px; padding: 0 5px 0 6px; display: flex; align-items: center;
    gap: 9px; font-size: 8.5px; color: var(--ink-soft); }
  .chip svg { width: 12px; height: 12px; }
  .chip.active { background: var(--brand); border-color: var(--brand); color: #fff; font-weight: 600; padding: 0 5px; }
  .chevron { left: 220px; top: 80px; width: 9px; height: 9px; }
  .divider { left: 0; top: 93px; width: 448px; height: 1px; background: var(--line); }
  .last-used-title { left: 22px; top: 106px; }
  .folder-grid { left: 15px; top: 144px; display: grid; grid-template-columns: repeat(3, 127px); column-gap: 18px; row-gap: 10px; }
  .folder { height: 29px; background: var(--card-bg); border-radius: 6px; display: flex; align-items: center; padding: 0 12px 0 9px;
    gap: 13px; font-size: 8.5px; color: var(--ink); }
  .folder svg { width: 13px; height: 13px; flex: none; }
  .folder .kebab { margin-left: auto; }
  .folder.active { background: var(--brand); color: #fff; font-weight: 600; }

  .side-card { left: 642px; width: 169px; background: var(--surface); border-radius: 6px; padding: 10px 15px; }
  .details { top: 74px; height: 241px; }
  .details p { font-size: 8.5px; color: var(--ink-soft); }
  .details .meta-1 { margin-top: 42px; }
  .details .meta-2 { margin-top: 12px; }
  .update { top: 336px; height: 111px; }
  .update ul { list-style: none; margin-top: 22px; font-size: 8.5px; color: var(--muted); }
  .update li + li { margin-top: 9px; }
</style>
</head>
<body>

<section class="login abs">
  <div class="login-showcase abs">
    <div class="showcase-art abs" role="img" aria-label="Illustration of a person at a laptop unlocking a password-protected folder vault, with padlocks and masked passwords around"></div>
    <div class="carousel-dots abs"><span class="active"></span><span></span><span></span></div>
  </div>

  <div class="brand login-brand abs"><span class="brand-mark"></span>Lumen Keyvault</div>
  <h1 class="welcome abs">Welcome Back!</h1>

  <label class="field field-email abs">
    <svg viewBox="0 0 12 12" fill="none" stroke="#8a9099" stroke-width="1"><rect x="1" y="2.5" width="10" height="7" rx="1"/><path d="M1.5 3l4.5 3.5 4.5-3.5"/></svg>
    Enter your email
  </label>
  <label class="field field-password abs">
    <svg viewBox="0 0 12 12" fill="none" stroke="#8a9099" stroke-width="1"><rect x="2" y="5.5" width="8" height="5.5" rx="1"/><path d="M4 5.5V4a2 2 0 0 1 4 0v1.5"/></svg>
    Enter password
    <span class="link">Forgot Password?</span>
  </label>

  <div class="btn-primary btn-login abs">Login</div>
  <div class="or abs">OR</div>
  <div class="btn-alt abs">Continue with Nimbly</div>
  <div class="signup-prompt abs">Don't have an account?</div>
  <div class="btn-primary btn-signup abs">Sign up</div>

  <div class="help abs"><span class="help-mark"></span>Help</div>
</section>

<section class="vault abs">
  <div class="brand vault-brand abs"><span class="brand-mark"></span>Lumen Keyvault</div>
  <div class="search abs">Search</div>
  <div class="btn-primary btn-add abs">
    <svg viewBox="0 0 16 16" fill="none" stroke="#fff" stroke-width="1.5"><rect x="2" y="4" width="10" height="10" rx="1"/><path d="M4.5 7.5h5M4.5 10.5h5M13 1v5M10.5 3.5h5"/></svg>
    Add
  </div>
  <svg class="bell abs" viewBox="0 0 14 14" fill="#5b6068"><path d="M7 1.5a4 4 0 0 0-4 4V9L1.8 10.5h10.4L11 9V5.5a4 4 0 0 0-4-4z"/><circle cx="7" cy="12.2" r="1.3"/></svg>

  <nav>
    <div class="nav-item nav-vault active abs">
      <svg viewBox="0 0 14 14" fill="#fff"><path d="M7 1.5L1.5 6v6.5h4V9h3v3.5h4V6z"/></svg>Vault
    </div>
    <div class="nav-item nav-shared abs">
      <svg viewBox="0 0 14 14" fill="#2a2e34"><circle cx="5" cy="4.5" r="2.2"/><circle cx="10" cy="4.5" r="1.9"/><path d="M0.5 12c0-2.5 2-3.8 4.5-3.8s4.5 1.3 4.5 3.8z"/><path d="M10 8.3c2 0 3.5 1.2 3.5 3.7h-3c0-1.6-.5-2.8-1.5-3.5z"/></svg>Shared with me
    </div>
    <div class="nav-item nav-trash abs">
      <svg viewBox="0 0 14 14" fill="none" stroke="#2a2e34" stroke-width="1.6"><path d="M2 3h10M5 3V1.5h4V3M3.2 3l.6 9.5h6.4l.6-9.5M6 5.5v5M8 5.5v5"/></svg>Trash
    </div>
  </nav>

  <div class="account abs">
    <svg viewBox="0 0 14 14" fill="#2a2e34"><path d="M6 0.8h2l.3 1.8 1.3.6 1.5-1.1 1.4 1.4-1.1 1.5.6 1.3 1.8.3v2l-1.8.3-.6 1.3 1.1 1.5-1.4 1.4-1.5-1.1-1.3.6-.3 1.8H6l-.3-1.8-1.3-.6-1.5 1.1-1.4-1.4 1.1-1.5-.6-1.3L.2 8V6l1.8-.3.6-1.3-1.1-1.5 1.4-1.4 1.5 1.1 1.3-.6zM7 4.6a2.4 2.4 0 1 0 0 4.8 2.4 2.4 0 0 0 0-4.8z"/></svg>
    <span class="avatar" role="img" aria-label="User profile photo"></span>
    My Account
  </div>

  <div class="main-panel abs">
    <h2 class="panel-title category-title abs">Category</h2>
    <div class="kebab category-menu abs"><i></i><i></i><i></i></div>

    <div class="chips abs">
      <div class="chip active"><svg viewBox="0 0 12 12" fill="#fff"><path d="M.5 2h4l1 1.2h6v7.3H.5z"/></svg>General</div>
      <div class="chip"><svg viewBox="0 0 12 12" fill="#5b6068"><path d="M4 1.5h4V3h3.5v7.5H.5V3H4zM5 2.5V3h2v-.5z"/></svg>Work</div>
      <div class="chip"><svg viewBox="0 0 12 12" fill="#5b6068"><path d="M.5 2h4l1 1.2h6v7.3H.5z"/><circle cx="6" cy="6" r="1.2" fill="#fff"/><path d="M3.8 9.2c0-1.3 1-1.9 2.2-1.9s2.2.6 2.2 1.9z" fill="#fff"/></svg>Shared with me</div>
      <div class="chip"><svg viewBox="0 0 12 12" fill="none" stroke="#5b6068" stroke-width="1"><rect x="1" y="3.5" width="10" height="7" rx="1"/><path d="M4 3.5V1.8h4v1.7M1 6.5h10"/></svg>Travel</div>
      <div class="chip"><svg viewBox="0 0 12 12" fill="#5b6068"><path d="M.5 2h11v8H.5z"/><path d="M1 2.5l5 3.5 5-3.5" stroke="#fff" stroke-width="1" fill="none"/></svg>Mail</div>
    </div>
    <svg class="chevron abs" viewBox="0 0 10 10" fill="none" stroke="#5b6068" stroke-width="1.3"><path d="M2 3.5l3 3 3-3"/></svg>
    <div class="divider abs"></div>

    <h2 class="panel-title last-used-title abs">Last Used</h2>
    <div class="folder-grid abs">
      <div class="folder"><svg viewBox="0 0 14 14" fill="none" stroke="currentColor" stroke-width="1.2"><path d="M1 2.5h4.5l1.2 1.5H13v7.5H1z"/></svg>Social Media<div class="kebab"><i></i><i></i><i></i></div></div>
      <div class="folder"><svg viewBox="0 0 14 14" fill="none" stroke="currentColor" stroke-width="1.2"><path d="M1 2.5h4.5l1.2 1.5H13v7.5H1z"/></svg>Social Media<div class="kebab"><i></i><i></i><i></i></div></div>
      <div class="folder"><svg viewBox="0 0 14 14" fill="none" stroke="currentColor" stroke-width="1.2"><path d="M1 2.5h4.5l1.2 1.5H13v7.5H1z"/></svg>Social Media<div class="kebab"><i></i><i></i><i></i></div></div>

      <div class="folder active"><svg viewBox="0 0 14 14" fill="none" stroke="currentColor" stroke-width="1.2"><path d="M1 2.5h4.5l1.2 1.5H13v7.5H1z"/></svg>Chirper<div class="kebab"><i></i><i></i><i></i></div></div>
      <div class="folder"><svg viewBox="0 0 14 14" fill="none" stroke="currentColor" stroke-width="1.2"><path d="M1 2.5h4.5l1.2 1.5H13v7.5H1z"/></svg>Chirper<div class="kebab"><i></i><i></i><i></i></div></div>
      <div class="folder"><svg viewBox="0 0 14 14" fill="none" stroke="currentColor" stroke-width="1.2"><path d="M1 2.5h4.5l1.2 1.5H13v7.5H1z"/></svg>Chirper<div class="kebab"><i></i><i></i><i></i></div></div>

      <div class="folder"><svg viewBox="0 0 14 14" fill="none" stroke="currentColor" stroke-width="1.2"><path d="M1 2.5h4.5l1.2 1.5H13v7.5H1z"/></svg>Work<div class="kebab"><i></i><i></i><i></i></div></div>
      <div class="folder"><svg viewBox="0 0 14 14" fill="none" stroke="currentColor" stroke-width="1.2"><path d="M1 2.5h4.5l1.2 1.5H13v7.5H1z"/></svg>Work<div class="kebab"><i></i><i></i><i></i></div></div>
      <div class="folder"><svg viewBox="0 0 14 14" fill="none" stroke="currentColor" stroke-width="1.2"><path d="M1 2.5h4.5l1.2 1.5H13v7.5H1z"/></svg>Work<div class="kebab"><i></i><i></i><i></i></div></div>

      <div class="folder"><svg viewBox="0 0 14 14" fill="none" stroke="currentColor" stroke-width="1.2"><path d="M1 2.5h4.5l1.2 1.5H13v7.5H1z"/></svg>Threadly<div class="kebab"><i></i><i></i><i></i></div></div>
      <div class="folder"><svg viewBox="0 0 14 14" fill="none" stroke="currentColor" stroke-width="1.2"><path d="M1 2.5h4.5l1.2 1.5H13v7.5H1z"/></svg>Threadly<div class="kebab"><i></i><i></i><i></i></div></div>
      <div class="folder"><svg viewBox="0 0 14 14" fill="none" stroke="currentColor" stroke-width="1.2"><path d="M1 2.5h4.5l1.2 1.5H13v7.5H1z"/></svg>Threadly<div class="kebab"><i></i><i></i><i></i></div></div>

      <div class="folder"><svg viewBox="0 0 14 14" fill="none" stroke="currentColor" stroke-width="1.2"><path d="M1 2.5h4.5l1.2 1.5H13v7.5H1z"/></svg>Banking<div class="kebab"><i></i><i></i><i></i></div></div>
      <div class="folder"><svg viewBox="0 0 14 14" fill="none" stroke="currentColor" stroke-width="1.2"><path d="M1 2.5h4.5l1.2 1.5H13v7.5H1z"/></svg>Banking<div class="kebab"><i></i><i></i><i></i></div></div>
      <div class="folder"><svg viewBox="0 0 14 14" fill="none" stroke="currentColor" stroke-width="1.2"><path d="M1 2.5h4.5l1.2 1.5H13v7.5H1z"/></svg>Banking<div class="kebab"><i></i><i></i><i></i></div></div>

      <div class="folder"><svg viewBox="0 0 14 14" fill="none" stroke="currentColor" stroke-width="1.2"><path d="M1 2.5h4.5l1.2 1.5H13v7.5H1z"/></svg>Authentication<div class="kebab"><i></i><i></i><i></i></div></div>
      <div class="folder"><svg viewBox="0 0 14 14" fill="none" stroke="currentColor" stroke-width="1.2"><path d="M1 2.5h4.5l1.2 1.5H13v7.5H1z"/></svg>Authentication<div class="kebab"><i></i><i></i><i></i></div></div>
      <div class="folder"><svg viewBox="0 0 14 14" fill="none" stroke="currentColor" stroke-width="1.2"><path d="M1 2.5h4.5l1.2 1.5H13v7.5H1z"/></svg>Authentication<div class="kebab"><i></i><i></i><i></i></div></div>
    </div>
  </div>

  <aside class="side-card details abs">
    <h2 class="panel-title">Details</h2>
    <p class="meta-1">Folder name: Chirper</p>
    <p class="meta-2">Created on: 03 June 2023</p>
  </aside>

  <aside class="side-card update abs">
    <h2 class="panel-title">Update</h2>
    <ul><li>What's new</li><li>Blog</li><li>Help</li></ul>
  </aside>
</section>

</body>
</html>
```